App for Basket Haven to Link to Our Site and do simple things

After Simple design that acts as an interface for our customers. the app does simple things.

*Links to our Webpage - www.baskethaven.com.au
Shopping cart will live on our website

*People can call us from App - 1800 742 918
*People can send us a message from App
*We can Send Push Notifications
*Page dedicated to specials

*Link to Diary/Calendar (or create a inbuilt calendar) to remind people of upcoming birthdays/Anniversaries*** Reminder set 7 to 15 days before event to give enough time to send a gift.

Target Market(s)

People can download the app so they have our details handy on their phone

Industry/Entity Type

Retail

Colors

Designer to choose colors to be used in the design.

Requirements
Must have
• *** PREFER AN APP DESIGNER WHO CAN CODE THE APP AS WELL***
• Link to Diary/Calendar (or create a inbuilt calendar) to remind people of upcoming birthdays/Anniversaries*** Reminder set 7 to 15 days before event to give enough time to send a gift.
• Need to be able to send push notifications with special coupon codes
• Need to be able to send Push notifications
• Our Logo/as it or modified
• a map for directions 518 Tallowgate Road, West Brunswick VIC 3055
• Need to be able to change the Banner as needed

```html
<!DOCTYPE html>
<html lang="en">
<head>
<meta charset="utf-8">
<title>Basket Haven – Home</title>
<link rel="stylesheet" href="https://fonts.googleapis.com/css2?family=Open+Sans:wght@300;400;600;700&family=Oswald:wght@300;500;600&display=swap">
<style>
  :root {
    --ink: #1d1d1f;
    --banner-bg: #f3f4f6;
    --grid-bg: #eceef0;
    --card: #ffffff;
    --muted: #7a7a7a;
    --price: #25348a;
    --accent-green: #3cc04a;
    --heart-red: #e8121c;
    --icon-grey: #9a9a9a;
    --brand: #1f3a8f;
  }
  * { box-sizing: border-box; margin: 0; padding: 0; }
  html, body { width: 705px; height: 1200px; overflow: hidden; }
  body {
    position: relative;
    background: var(--grid-bg);
    font-family: "Open Sans", Arial, sans-serif;
    color: var(--ink);
  }

  .status-bar {
    position: absolute; left: 0; top: 0; width: 705px; height: 43px;
    background: var(--card);
    display: flex; align-items: center; justify-content: space-between;
    padding: 0 18px; font-size: 23px; font-weight: 400;
  }
  .status-left, .status-right { display: flex; align-items: center; gap: 8px; }
  .signal { display: flex; gap: 3px; }
  .signal span { width: 9px; height: 9px; border-radius: 50%; background: var(--ink); }
  .status-time { position: absolute; left: 0; right: 0; text-align: center; pointer-events: none; }

  .app-header {
    position: absolute; left: 0; top: 43px; width: 705px; height: 78px;
    background: var(--card);
    box-shadow: 0 2px 4px rgba(0,0,0,0.08);
    display: flex; align-items: center; justify-content: center;
    z-index: 2;
  }
  .menu-button { position: absolute; left: 28px; top: 22px; }
  .search-button { position: absolute; right: 30px; top: 20px; }
  .brand-name {
    display: flex; align-items: center; gap: 10px;
    font-size: 30px; font-weight: 600; color: var(--brand);
  }
  .brand-mark { width: 18px; height: 18px; background: var(--brand); }

  .specials-banner {
    position: absolute; left: 0; top: 121px; width: 705px; height: 313px;
    background: var(--banner-bg);
  }
  .discount {
    position: absolute; left: 67px; top: 90px;
    font-family: "Oswald", "Arial Narrow", sans-serif;
    font-weight: 600; font-size: 64px; line-height: 1; color: #2c2c2e;
    letter-spacing: -1px;
  }
  .off-tag {
    position: absolute; left: 283px; top: 58px; width: 103px; height: 107px;
    border: 2px solid var(--accent-green);
    display: flex; align-items: flex-end; justify-content: center; padding-bottom: 10px;
    font-family: "Oswald", "Arial Narrow", sans-serif;
    font-weight: 300; font-size: 60px; line-height: 1; color: #2c2c2e;
    background: var(--banner-bg);
  }
  .off-tag-bow {
    position: absolute; left: 310px; top: 40px; width: 48px; height: 30px;
    border-radius: 14px; background: var(--accent-green);
  }
  .tagline {
    position: absolute; left: 67px; top: 164px;
    font-size: 22px; font-weight: 400; color: #3a3a3c;
  }
  .call-note {
    position: absolute; left: 67px; top: 204px; width: 260px;
    font-size: 11px; line-height: 1.35; color: #6a6a6a;
  }
  .banner-photo {
    position: absolute; left: 432px; top: 38px; width: 232px; height: 240px;
    background: linear-gradient(160deg, #e4e4e6 0%, #2d2d30 45%, #8e2a2a 80%, #d7b35a 100%);
    border-radius: 4px;
  }

  .product-grid {
    position: absolute; left: 10px; top: 446px; width: 687px;
    display: grid; grid-template-columns: 339px 339px; column-gap: 9px; row-gap: 12px;
  }
  .product-card {
    position: relative; height: 438px; background: var(--card);
    box-shadow: 0 1px 2px rgba(0,0,0,0.06);
  }
  .product-photo { position: absolute; left: 20px; top: 32px; width: 299px; height: 260px; border-radius: 2px; }
  .photo-baby { background: linear-gradient(135deg, #f4d9e6 0%, #bfe6ea 45%, #2f2f32 75%, #e9e9ea 100%); }
  .photo-wine { background: linear-gradient(135deg, #2b1d1e 0%, #d7c35c 35%, #1e1e20 60%, #b03a2e 100%); }
  .photo-divider { position: absolute; left: 0; right: 0; top: 321px; height: 1px; background: #e6e6e8; }
  .favourite { position: absolute; right: 14px; top: 16px; }
  .product-name {
    position: absolute; left: 19px; top: 338px;
    font-size: 26px; font-weight: 300; color: var(--muted);
  }
  .product-price {
    position: absolute; left: 19px; top: 380px;
    font-size: 28px; font-weight: 400; color: var(--price);
  }
  .add-to-cart { position: absolute; right: 20px; top: 388px; }
</style>
</head>
<body>

  <div class="status-bar">
    <div class="status-left">
      <div class="signal"><span></span><span></span><span></span><span></span><span></span></div>
      <span>Telwave</span>
      <svg width="22" height="16" viewBox="0 0 22 16"><path d="M1 5a15 15 0 0 1 20 0M4.5 8.5a10 10 0 0 1 13 0M8 12a5 5 0 0 1 6 0" fill="none" stroke="#1d1d1f" stroke-width="2.2" stroke-linecap="round"/><circle cx="11" cy="14.5" r="1.5" fill="#1d1d1f"/></svg>
    </div>
    <div class="status-time">9:23 AM</div>
    <div class="status-right">
      <svg width="16" height="16" viewBox="0 0 16 16"><path d="M15 1L1 7l6 2 2 6z" fill="#1d1d1f"/></svg>
      <span>66%</span>
      <svg width="42" height="20" viewBox="0 0 42 20"><rect x="1" y="1" width="36" height="18" rx="4" fill="none" stroke="#1d1d1f" stroke-width="1.6"/><rect x="4" y="4" width="22" height="12" rx="2" fill="#1d1d1f"/><rect x="38.5" y="7" width="2.5" height="6" rx="1" fill="#1d1d1f"/></svg>
    </div>
  </div>

  <header class="app-header">
    <svg class="menu-button" width="44" height="34" viewBox="0 0 44 34" aria-label="Menu"><path d="M4 3h36M8 17h32M4 31h36" stroke="#2a2a2c" stroke-width="3" stroke-linecap="round"/></svg>
    <div class="brand-name"><span class="brand-mark"></span>Basket Haven</div>
    <svg class="search-button" width="40" height="40" viewBox="0 0 40 40" aria-label="Search"><circle cx="17" cy="17" r="13" fill="none" stroke="#2a2a2c" stroke-width="2.6"/><path d="M26.5 26.5L37 37" stroke="#2a2a2c" stroke-width="2.6" stroke-linecap="round"/></svg>
  </header>

  <section class="specials-banner">
    <div class="discount">40-60%</div>
    <div class="off-tag">OFF</div>
    <div class="off-tag-bow" role="img" aria-label="Green gift bow"></div>
    <p class="tagline">You can't refuse</p>
    <p class="call-note">Call our staff on 1800 742 918 and they will be happy to help you select a gift.</p>
    <div class="banner-photo" role="img" aria-label="Gift box with chocolates, wine and treats tied with a black ribbon"></div>
  </section>

  <main class="product-grid">
    <article class="product-card">
      <div class="product-photo photo-baby" role="img" aria-label="Baby gift hamper with socks, bath wash, shampoo and soap bar"></div>
      <svg class="favourite" width="30" height="28" viewBox="0 0 30 28" aria-label="Saved"><path d="M15 27S1 18 1 9a7 7 0 0 1 14-2 7 7 0 0 1 14 2c0 9-14 18-14 18z" fill="var(--heart-red)"/></svg>
      <div class="photo-divider"></div>
      <h2 class="product-name">Gift Hamper Box</h2>
      <p class="product-price">$41</p>
      <svg class="add-to-cart" width="32" height="28" viewBox="0 0 32 28" aria-label="Add to cart"><path d="M1 2h5l4 16h17l3-11H8" fill="none" stroke="var(--icon-grey)" stroke-width="2" stroke-linejoin="round"/><path d="M10 10h18M11 14h16" stroke="var(--icon-grey)" stroke-width="1.5"/><circle cx="12" cy="24" r="2.2" fill="var(--icon-grey)"/><circle cx="25" cy="24" r="2.2" fill="var(--icon-grey)"/></svg>
    </article>

    <article class="product-card">
      <div class="product-photo photo-wine" role="img" aria-label="Red and white wine bottles with olives, quince paste and crackers in a gift box"></div>
      <svg class="favourite" width="30" height="28" viewBox="0 0 30 28" aria-label="Save"><path d="M15 26S2 17.5 2 9.5a6.5 6.5 0 0 1 13-2 6.5 6.5 0 0 1 13 2c0 8-13 16.5-13 16.5z" fill="none" stroke="#b5b5b8" stroke-width="2"/></svg>
      <div class="photo-divider"></div>
      <h2 class="product-name">Ridgefall Wine</h2>
      <p class="product-price">$100</p>
      <svg class="add-to-cart" width="32" height="28" viewBox="0 0 32 28" aria-label="Add to cart"><path d="M1 2h5l4 16h17l3-11H8" fill="none" stroke="var(--icon-grey)" stroke-width="2" stroke-linejoin="round"/><path d="M10 10h18M11 14h16" stroke="var(--icon-grey)" stroke-width="1.5"/><circle cx="12" cy="24" r="2.2" fill="var(--icon-grey)"/><circle cx="25" cy="24" r="2.2" fill="var(--icon-grey)"/></svg>
    </article>

    <article class="product-card">
      <div class="product-photo photo-baby" role="img" aria-label="Baby gift hamper with socks, bath wash, shampoo and soap bar"></div>
      <svg class="favourite" width="30" height="28" viewBox="0 0 30 28" aria-label="Saved"><path d="M15 27S1 18 1 9a7 7 0 0 1 14-2 7 7 0 0 1 14 2c0 9-14 18-14 18z" fill="var(--heart-red)"/></svg>
      <div class="photo-divider"></div>
      <h2 class="product-name">Gift Hamper Box</h2>
    </article>

    <article class="product-card">
      <div class="product-photo photo-wine" role="img" aria-label="Red and white wine bottles with olives, quince paste and crackers in a gift box"></div>
      <svg class="favourite" width="30" height="28" viewBox="0 0 30 28" aria-label="Save"><path d="M15 26S2 17.5 2 9.5a6.5 6.5 0 0 1 13-2 6.5 6.5 0 0 1 13 2c0 8-13 16.5-13 16.5z" fill="none" stroke="#b5b5b8" stroke-width="2"/></svg>
      <div class="photo-divider"></div>
      <h2 class="product-name">Ridgefall Wine</h2>
    </article>
  </main>

</body>
</html>
```